Pellmark Ridgeway LLC stationery, business card and web page design.

i need a full set of stationery designed using the name "Pellmark Ridgeway LLC" with a tag line "construction consulting services". using the uploaded monkey icon as the logo.

i like the colors orange, green and black in general but im not limited to that. the company offers consulting services to various types of construction businesses.

i travel around the country in a 4x4 camper offering consulting services and technical training short term and long to various types of construction companies.

Construction Company

Peter Lund
p.lund@pellmarkridgeway.example
2748 Fenwick Rd
Maple Glen, NY 10943
555 014 3627

list these services on the card.

Business Consulting
Capital Investments
Marketing Implementations
Technical Training

1 page

Designer to choose colors to be used in the design.

• company info and use of the monkey icon i provided.
• a fun but professional design
• the color red

```html
<!DOCTYPE html>
<html lang="en">
<head>
<meta charset="utf-8">
<title>Pellmark Ridgeway LLC – Stationery Set</title>
<link href="https://fonts.googleapis.com/css2?family=Varela+Round&family=Montserrat:wght@400;500;600&display=swap" rel="stylesheet">
<style>
  :root{
    --backdrop:#3c2316;
    --paper:#ffffff;
    --orange:#f0602b;
    --ink:#111111;
    --night:#0d0d0d;
    --muted:#c9c9c9;
    --label:#f2f2f2;
  }
  *{margin:0;padding:0;box-sizing:border-box}
  html,body{width:1200px;height:770px;overflow:hidden;background:var(--backdrop)}
  body{position:relative;font-family:"Montserrat",Arial,sans-serif;color:var(--ink)}
  .piece{position:absolute;background:var(--paper);box-shadow:2px 3px 4px rgba(0,0,0,.45);overflow:hidden}
  .label{position:absolute;color:var(--label);font-size:13px;letter-spacing:.5px;transform:translateX(-50%);white-space:nowrap}
  .mark{position:absolute;border-radius:50%;background:var(--ink)}
  .brand-name{position:absolute;font-family:"Varela Round",Arial,sans-serif;color:var(--orange);white-space:nowrap}
  .tagline{position:absolute;white-space:nowrap;letter-spacing:.18em}
  .hazard{position:absolute;left:0;right:0;background:repeating-linear-gradient(120deg,var(--orange) 0 28px,var(--night) 28px 46px)}
  .accent{color:var(--orange)}
  .small{position:absolute;white-space:nowrap}

  /* letterhead */
  .letterhead{left:62px;top:79px;width:489px;height:633px}
  .letterhead .footer{position:absolute;left:0;right:0;bottom:0;height:43px;background:var(--night);color:#fff;font-size:7.5px;line-height:11px}

  /* business cards */
  .card{width:202px;height:114px}
  .front-one{left:587px;top:78px}
  .front-two{left:841px;top:78px}
  .back-one{left:586px;top:206px;background:var(--orange)}
  .back-two{left:839px;top:204px}
  .card .tiny{font-size:5px;line-height:7px}

  /* envelope */
  .flap{position:absolute;left:587px;top:380px;width:560px;height:65px}
  .envelope{left:583px;top:459px;width:560px;height:253px}
</style>
</head>
<body>

<!-- Letterhead -->
<section class="piece letterhead" aria-label="Letterhead">
  <div class="mark" style="left:32px;top:32px;width:56px;height:56px"></div>
  <div class="brand-name" style="left:94px;top:49px;font-size:17.5px">Pellmark Ridgeway LLC</div>
  <div class="tagline" style="left:95px;top:75px;font-size:8px">construction consulting services</div>
  <div class="hazard" style="bottom:43px;height:8px"></div>
  <div class="footer">
    <div class="small" style="left:25px;top:13px">00000 City name, Country name 00000,<br><span class="accent">Email:</span> info@pellmarkridgewayllc.example</div>
    <div class="small" style="left:307px;top:13px"><span class="accent">Phone:</span> 012.345.6789<br>www.pellmarkridgewayllc.example</div>
  </div>
  <div class="mark" style="left:213px;top:552px;width:62px;height:62px"></div>
</section>

<!-- Business cards -->
<div class="label" style="left:704px;top:47px">Front option-1</div>
<section class="piece card front-one" aria-label="Business card front, option 1">
  <div class="mark" style="left:11px;top:9px;width:32px;height:32px"></div>
  <div class="brand-name" style="left:44px;top:19px;font-size:9.5px">Pellmark Ridgeway LLC</div>
  <div class="tagline" style="left:44px;top:33px;font-size:4.3px">construction consulting services</div>
  <div class="small" style="left:10px;top:69px;font-size:6px;border-bottom:.6px solid var(--orange);padding-bottom:1px">Peter Lund, <span style="font-size:4.3px">Designation</span></div>
  <div class="small tiny" style="left:10px;top:85px">2748 Fenwick Rd,<br>Maple Glen, NY 10943.<br><span class="accent">P:</span> 555 014 3627<br><span class="accent">E:</span> p.lund@pellmarkridgeway.example</div>
  <div class="mark" style="left:138px;top:67px;width:28px;height:28px;background:var(--muted)"></div>
  <div class="small tiny accent" style="left:108px;top:98px">www.pellmarkridgewayllc.example</div>
  <div class="hazard" style="bottom:0;height:8px"></div>
</section>

<div class="label" style="left:938px;top:52px">Front option-2</div>
<section class="piece card front-two" aria-label="Business card front, option 2">
  <div class="mark" style="left:30px;top:12px;width:32px;height:32px"></div>
  <div class="brand-name" style="left:66px;top:22px;font-size:9.5px">Pellmark Ridgeway LLC</div>
  <div class="tagline" style="left:66px;top:36px;font-size:4.3px">construction consulting services</div>
  <div class="small tiny accent" style="left:0;right:0;top:61px;text-align:center">www.pellmarkridgewayllc.example</div>
  <div class="small" style="left:0;right:0;top:70px;text-align:center;font-size:6px">Peter Lund</div>
  <div class="hazard" style="bottom:24px;height:7px"></div>
  <div style="position:absolute;left:0;right:0;bottom:0;height:24px;background:var(--night);color:#fff;text-align:center;padding-top:5px" class="tiny">2748 Fenwick Rd, Maple Glen, NY 10943,<br>Email: p.lund@pellmarkridgeway.example</div>
</section>

<section class="piece card back-one" aria-label="Business card back, option 1">
  <div class="mark" style="left:80px;top:34px;width:40px;height:40px"></div>
  <div class="small" style="left:0;right:0;top:84px;text-align:center;font-size:7px;font-weight:600;color:var(--ink)">www.<span style="color:#fff">pellmarkridgewayllc</span>.example</div>
</section>
<div class="label" style="left:682px;top:330px">Back 1</div>

<section class="piece card back-two" aria-label="Business card back, option 2">
  <div class="mark" style="left:86px;top:30px;width:32px;height:32px"></div>
  <div class="brand-name" style="left:0;right:0;top:67px;text-align:center;font-size:7.5px">Pellmark Ridgeway LLC</div>
  <div class="tagline" style="left:0;right:0;top:78px;text-align:center;font-size:3.8px">construction consulting services</div>
</section>
<div class="label" style="left:945px;top:328px">Back 2</div>

<!-- Envelope -->
<svg class="flap" viewBox="0 0 560 65" aria-label="Envelope flap">
  <path d="M0 0 H560 L532 50 Q524 63 505 63 H70 Q50 63 35 52 Z" fill="var(--orange)" style="filter:drop-shadow(2px 3px 2px rgba(0,0,0,.4))"/>
  <circle cx="280" cy="31" r="21" fill="var(--ink)"/>
</svg>

<section class="piece envelope" aria-label="Envelope">
  <div class="mark" style="left:15px;top:15px;width:50px;height:50px"></div>
  <div class="brand-name" style="left:66px;top:31px;font-size:15px">Pellmark Ridgeway LLC</div>
  <div class="tagline" style="left:67px;top:54px;font-size:7px">construction consulting services</div>
  <div class="small" style="left:21px;top:226px;font-size:7.5px;color:#444">
    <span class="accent" style="font-weight:600">Pellmark Ridgeway LLC,</span>&nbsp;&nbsp;&nbsp; 00000 City name, Country name 00000,&nbsp;&nbsp;&nbsp; <span class="accent">Phone:</span> 012.345.6789&nbsp;&nbsp;&nbsp; <span class="accent">Email:</span> info@pellmarkridgewayllc.example
  </div>
  <div class="hazard" style="bottom:0;height:14px"></div>
</section>

</body>
</html>
```